Construction company- stationary project
business card, letterhead, envelopes, presentation folder
Construction company- stationary project -
Creative Brief
Professional
Brent Halloway
38 Percival Ln. Millbrook, NY 12545
brent.halloway@ridgefold-builders.com
www.ridgefold-builders.com
Residential contractor focused on design build, custom, and restoration projects. Emphasizing team concept
open to ideas possibly the logo

```html
<!DOCTYPE html>
<html lang="en">
<head>
<meta charset="utf-8">
<title>Ridgefold Builders — Stationery</title>
<link rel="stylesheet" href="https://fonts.googleapis.com/css2?family=Cinzel:wght@400;600&display=swap">
<style>
  :root {
    --bg: #e4e4e4;
    --paper: #ffffff;
    --brown-deep: #2e1008;
    --brown: #5a2210;
    --copper: #a9522a;
    --ink: #4a2214;
    --ink-soft: #6b4a3c;
    --ghost: rgba(120, 80, 60, 0.07);
    --mission: #e9c7ad;
  }
  * { box-sizing: border-box; margin: 0; padding: 0; }
  html, body { width: 1200px; height: 876px; overflow: hidden; }
  body {
    background: var(--bg);
    font-family: "Cinzel", "Times New Roman", serif;
    color: var(--ink);
    position: relative;
  }
  .piece { position: absolute; background: var(--paper); overflow: hidden; box-shadow: 0 2px 8px rgba(0,0,0,0.18); }
  .band {
    position: absolute; left: 0; right: 0; top: 0;
    background: radial-gradient(ellipse at 50% 40%, var(--copper) 0%, var(--brown) 45%, var(--brown-deep) 100%);
  }
  .brand {
    position: absolute; left: 0; right: 0; text-align: center;
    font-weight: 600; color: var(--brown); letter-spacing: 0.04em;
    display: flex; align-items: center; justify-content: center; gap: 8px;
    white-space: nowrap;
  }
  .brand-dot { width: 9px; height: 9px; border-radius: 50%; background: var(--copper); flex: none; }

  /* Letterhead */
  .letterhead { left: 53px; top: 36px; width: 470px; height: 804px; }
  .letterhead .band { height: 62px; }
  .letterhead .brand { top: 84px; font-size: 22px; }
  .letterhead .ghost-name {
    position: absolute; left: 34px; top: 250px; font-size: 48px; font-weight: 400;
    color: var(--ghost); letter-spacing: 0.02em; white-space: nowrap;
  }
  .letterhead .footer {
    position: absolute; left: 0; right: 0; bottom: 28px; text-align: center;
    font-size: 10px; color: var(--ink-soft); letter-spacing: 0.04em; white-space: nowrap;
  }

  /* Business card front */
  .card-front { left: 547px; top: 29px; width: 298px; height: 168px; }
  .card-front .band { height: 38px; }
  .card-front .brand { top: 46px; font-size: 14px; gap: 6px; }
  .card-front .brand-dot { width: 7px; height: 7px; }
  .card-front .person {
    position: absolute; left: 0; right: 0; top: 82px; text-align: center;
    font-size: 13px; color: var(--ink);
  }
  .card-front .contact {
    position: absolute; left: 0; right: 0; top: 112px; text-align: center;
    font-size: 7px; line-height: 1.6; color: var(--ink-soft); letter-spacing: 0.03em;
  }

  /* Business card back */
  .card-back {
    left: 547px; top: 211px; width: 298px; height: 161px;
    background: radial-gradient(ellipse at 40% 50%, var(--copper) 0%, var(--brown) 50%, var(--brown-deep) 100%);
  }
  .card-back .mission {
    position: absolute; left: 36px; top: 52px; width: 240px;
    font-size: 8px; line-height: 1.7; color: var(--mission); letter-spacing: 0.04em;
  }

  /* Envelope */
  .envelope { left: 463px; top: 384px; width: 689px; height: 379px; }
  .envelope .band { height: 100px; }
  .envelope .band::after {
    content: ""; position: absolute; left: 0; right: 0; bottom: 0; height: 14px;
    background: linear-gradient(to bottom, rgba(0,0,0,0), rgba(0,0,0,0.25));
  }
  .envelope .flap-line {
    position: absolute; left: 0; right: 0; top: 14px; text-align: center;
    font-size: 9px; color: var(--mission); letter-spacing: 0.12em; opacity: 0.8;
  }
  .envelope .sender { position: absolute; left: 42px; top: 138px; }
  .envelope .sender .brand {
    position: static; justify-content: flex-start; font-size: 20px; gap: 7px;
  }
  .envelope .sender .address {
    margin-top: 12px; font-size: 11px; line-height: 1.5; color: var(--ink);
  }
</style>
</head>
<body>

  <section class="piece letterhead" aria-label="Letterhead">
    <div class="band"></div>
    <div class="brand"><span class="brand-dot"></span>Ridgefold Builders</div>
    <div class="ghost-name" aria-hidden="true">Ridgefold</div>
    <p class="footer">38 Percival Ln. Ashgrove, VT 05871 &nbsp;|&nbsp; www.ridgefold-builders.com</p>
  </section>

  <section class="piece card-front" aria-label="Business card front">
    <div class="band"></div>
    <div class="brand"><span class="brand-dot"></span>Ridgefold Builders</div>
    <p class="person">Brent Halloway</p>
    <p class="contact">
      38 Percival Ln. Ashgrove, VT 05871 &nbsp;|&nbsp; T: 802.555.0142<br>
      E: brent.halloway@ridgefold-builders.com<br>
      www.ridgefold-builders.com
    </p>
  </section>

  <section class="piece card-back" aria-label="Business card back">
    <p class="mission">
      Residential contractor focused on<br>
      design build, custom, and restoration projects.<br>
      Emphasizing team concept.
    </p>
  </section>

  <section class="piece envelope" aria-label="Envelope">
    <div class="band"><p class="flap-line">Design · Build · Custom · Restoration</p></div>
    <div class="sender">
      <div class="brand"><span class="brand-dot"></span>Ridgefold Builders</div>
      <p class="address">38 Percival Ln.<br>Ashgrove, VT 05871</p>
    </div>
  </section>

</body>
</html>
```